Letterhead design for ZENTORA company

I need an A4 letterhead design for my company "Zentora Electrical Products". I need the letterhead to match my current logo and business card designs. I would like it to be colourful and match the design of the business card in terms of the flowing line of colour where the information is.  

Target Market(s)

Adults aged 20 - 50 Upper middle class.

Industry/Entity Type

It Company

Requirements
Must have
• Must be A4 size and match my current logo and business card designs. Must be clean simple and eye catching.

• Must have the following information

• Zentora Electrical Products LTD
• 7 Ardley Close
• Chiswick
• London
• England
• W9 3QX
• Company No. 05316429
• VAT No. GB 627150384

• Telephone: 02081594360
• Mobile: 07815062247
• Email: info@zentora-goods.co.uk
Nice to have
• nice to have a wave of colour like the business card.
Should not have
• Should not be a different colour scheme to the business card and logo design.

```html
<!DOCTYPE html>
<html lang="en">
<head>
<meta charset="utf-8">
<title>Zentora Electrical Products – Letterhead</title>
<link rel="stylesheet" href="https://fonts.googleapis.com/css2?family=Carlito:wght@700&family=Open+Sans:wght@300;400&display=swap">
<style>
  :root {
    --blue-deep: #136f93;
    --blue-mid: #2596c4;
    --blue-bright: #33ade0;
    --label-blue: #1a5a96;
    --ink: #1f1f1f;
    --white: #ffffff;
    --paper-edge: #d6d6d6;
    --paper-centre: #ffffff;
  }
  * { margin: 0; padding: 0; box-sizing: border-box; }
  html, body { width: 849px; height: 1200px; overflow: hidden; background: #ffffff; }
  .letterhead {
    position: relative;
    width: 849px;
    height: 1200px;
    overflow: hidden;
    background: radial-gradient(ellipse 62% 55% at 50% 54%, var(--paper-centre) 0%, #f4f4f4 45%, var(--paper-edge) 100%);
    font-family: "Open Sans", sans-serif;
    color: var(--ink);
  }
  .header-band { position: absolute; top: 0; left: 0; width: 849px; height: 190px; display: block; }
  .brand {
    position: absolute;
    left: 42px;
    top: 33px;
    color: var(--white);
    font-family: "Open Sans", sans-serif;
    font-weight: 300;
    line-height: 1;
  }
  .brand-name { display: block; font-size: 46px; letter-spacing: 1px; }
  .brand-tagline { display: block; font-size: 17px; letter-spacing: 1.3px; margin-top: 5px; }
  .registration {
    position: absolute;
    right: 47px;
    top: 6px;
    text-align: center;
    color: var(--white);
    font-family: "Carlito", sans-serif;
    font-weight: 700;
    font-size: 16px;
    line-height: 21px;
  }
  .address {
    position: absolute;
    left: 0;
    width: 849px;
    top: 1143px;
    text-align: center;
    font-size: 15px;
  }
  .contacts {
    position: absolute;
    top: 1173px;
    left: 0;
    width: 849px;
    font-size: 15px;
    white-space: nowrap;
  }
  .contact { position: absolute; top: 0; }
  .contact-label { color: var(--label-blue); }
  .contact-phone { left: 69px; }
  .contact-mobile { left: 203px; }
  .contact-email { left: 337px; }
  .contact-web { left: 566px; }
</style>
</head>
<body>
<main class="letterhead">
  <svg class="header-band" viewBox="0 0 849 190" role="img" aria-label="Curved blue header band in the brand colours">
    <defs>
      <linearGradient id="band-fill" x1="0" y1="0" x2="1" y2="0">
        <stop offset="0" stop-color="#2596c4"/>
        <stop offset="0.45" stop-color="#33ade0"/>
        <stop offset="1" stop-color="#136f93"/>
      </linearGradient>
    </defs>
    <path d="M0 0 H849 V44 C700 120 420 172 0 160 Z" fill="url(#band-fill)"/>
  </svg>

  <div class="brand">
    <span class="brand-name">ZENTORA</span>
    <span class="brand-tagline">Electrical Products</span>
  </div>

  <div class="registration">
    <p>Company No. 05316429</p>
    <p>VAT No. GB 627150384</p>
  </div>

  <p class="address">7 Ardley Close, London, W9 3QX</p>

  <div class="contacts">
    <span class="contact contact-phone"><span class="contact-label">P.</span>02081594360</span>
    <span class="contact contact-mobile"><span class="contact-label">M.</span>07815062247</span>
    <span class="contact contact-email"><span class="contact-label">E.</span>info@zentora-goods.co.uk</span>
    <span class="contact contact-web"><span class="contact-label">W.</span>www.zentora-goods.co.uk</span>
  </div>
</main>
</body>
</html>
```